Therapeutic Counselling Practice Brochure

I have a new therapeutic counselling practice in Melbourne.

I am making peri natal issues my special interest area.

I need a brochure targeted at new parents or pregnant women and partners, struggling with the concept of parenting, depression, maybe do not even know about it.

The feel should be safe and strong. I love the KESTA website ( I do volunteer work with them)

Out of hours appointments and telephone counselling are important making my service very accessible.

Attached is an example for the content of the Brochure

Attached is an example for the content of the Brochure.

Target Market(s)

25 - 45 New Parents , expectant parents,families and friends of people struggling emotionally and mentally with and around being new parents

Requirements
Must have
• Feel of safety, somewhere to go for help, support, a conversation, soft ,strong
Nice to have
• mother and child, maybe parents and child, possibly a graphic, faceless

```html
<!DOCTYPE html>
<html lang="en">
<head>
<meta charset="utf-8">
<title>Depression During &amp; After Pregnancy – Brochure</title>
<link rel="stylesheet" href="https://fonts.googleapis.com/css2?family=Lobster+Two&family=Pathway+Gothic+One&family=Roboto+Condensed:wght@700&display=swap">
<style>
  :root {
    --page-bg: #ffffff;
    --paper: #ffffff;
    --fold-shade: #dcdcdc;
    --text-grey: #6a6a6a;
    --head-grey: #8b8b8b;
    --accent-blue: #8ccfdd;
    --wash-blue: #5fbde8;
    --wash-light: #a9dcf3;
    --wing-orange: #c8642a;
    --wing-purple: #7f7aa6;
    --wing-brown: #6b3a2a;
  }
  * { margin: 0; padding: 0; box-sizing: border-box; }
  html, body { width: 1200px; height: 900px; overflow: hidden; background: var(--page-bg); }
  .canvas { position: relative; width: 1200px; height: 900px; }

  .brochure {
    position: absolute; left: 75px; top: 78px; width: 1053px; height: 744px;
    background: var(--paper);
    box-shadow: 3px 4px 6px rgba(0,0,0,0.22);
    font-family: "Pathway Gothic One", "Arial Narrow", sans-serif;
    color: var(--text-grey);
  }
  .panel { position: absolute; top: 0; height: 100%; }
  .panel--left { left: 0; width: 350px; }
  .panel--middle {
    left: 350px; width: 350px;
    background: linear-gradient(90deg, #d9d9d9 0%, #f6f6f6 14%, #ffffff 45%, #f4f4f4 80%, #d4d4d4 100%);
  }
  .panel--right { left: 700px; width: 353px; }

  .abs { position: absolute; }
  .script { font-family: "Lobster Two", cursive; color: var(--accent-blue); font-weight: 400; }
  .body-copy { font-size: 14.5px; line-height: 19.5px; letter-spacing: 0.1px; }
  .lead { font-size: 21px; line-height: 24px; color: var(--accent-blue); }
  .subhead { font-family: "Roboto Condensed", "Arial Narrow", sans-serif; font-weight: 700; font-size: 15px; color: var(--head-grey); }

  .title { left: 25px; top: 40px; font-size: 44px; line-height: 52px; }
  .subtitle { left: 25px; top: 90px; font-size: 25px; line-height: 30px; }
  .intro { left: 25px; top: 145px; width: 300px; }
  .good-news { left: 25px; top: 243px; width: 310px; }
  .symptoms-head { left: 25px; top: 353px; }
  .symptoms-intro { left: 25px; top: 380px; }
  .symptom-list { left: 25px; top: 422px; list-style: none; }
  .symptom-list li { font-size: 14.5px; line-height: 24px; }
  .symptom-list li::before { content: "• "; }

  .impact { left: 25px; top: 205px; width: 300px; }
  .impact p + p { margin-top: 6px; }
  .wash { left: 10px; top: 350px; width: 316px; height: 138px; }
  .quote { left: 20px; top: 382px; width: 296px; text-align: center; color: #ffffff; font-size: 20px; line-height: 23px; }
  .treatment { left: 25px; top: 533px; width: 300px; }
  .no-discrimination { left: 25px; top: 600px; width: 320px; }

  .care-title-1 { left: 55px; top: 78px; font-size: 40px; line-height: 46px; }
  .care-title-2 { left: 150px; top: 122px; font-size: 40px; line-height: 46px; }
  .care-list { left: 25px; top: 166px; width: 320px; }
  .care-item { margin-bottom: 7px; }
  .care-item .subhead { display: block; margin-bottom: 1px; }
  .care-item p + p { margin-top: 6px; }

  .illustration { position: absolute; }
</style>
</head>
<body>
<div class="canvas">
  <article class="brochure">

    <section class="panel panel--left">
      <h1 class="abs script title">Depression...</h1>
      <h2 class="abs script subtitle">During &amp; After Pregnancy</h2>
      <p class="abs body-copy intro">Depression is more than just the “Baby Blues” (feeling weepy and irritable), or feeling “down in the dumps” for a few days. With depression, sad, anxious or empty feelings don’t go away. They interfere with your daily life and routines.</p>
      <p class="abs lead good-news">The good news is that most people with depression get better with treatment.</p>
      <h3 class="abs subhead symptoms-head">How do I know if I have depression?</h3>
      <p class="abs body-copy symptoms-intro">If you have any of the following symptoms<br>for more than two weeks:</p>
      <ul class="abs symptom-list">
        <li>Feeling restless or moody</li>
        <li>Feeling sad, hopeless and overwhelmed</li>
        <li>Crying</li>
        <li>Having no energy or motivation</li>
        <li>Eating too much or too little</li>
        <li>Sleeping too much or too little</li>
        <li>Withdrawing from family or friends</li>
        <li>Having memory problems</li>
        <li>Feeling worthless or guilty</li>
        <li>Experiencing headaches, aches and pains</li>
        <li>Having trouble focusing or making decisions</li>
        <li>Losing interest in pleasurable activities you used to enjoy.</li>
      </ul>
      <svg class="illustration" style="left:222px; top:428px;" width="130" height="200" viewBox="0 0 130 200" role="img" aria-label="Watercolour illustration of a rust-orange butterfly resting with wings raised">
        <defs>
          <linearGradient id="rustWing" x1="0" y1="0" x2="1" y2="1">
            <stop offset="0" stop-color="#e08a4a"/>
            <stop offset="1" stop-color="#6b3a2a"/>
          </linearGradient>
        </defs>
        <ellipse cx="58" cy="95" rx="40" ry="90" fill="url(#rustWing)" opacity="0.75"/>
      </svg>
    </section>

    <section class="panel panel--middle">
      <div class="abs body-copy impact">
        <p>Depression impacts on the whole family, including baby.</p>
        <p>You may feel guilty and a “not good enough mother”,<br>you may lose confidence.</p>
      </div>
      <svg class="illustration" style="left:205px; top:280px;" width="145" height="95" viewBox="0 0 145 95" role="img" aria-label="Watercolour illustration of a blue-violet butterfly in flight">
        <defs>
          <radialGradient id="violetWing" cx="0.5" cy="0.5" r="0.5">
            <stop offset="0" stop-color="#6f7fb8"/>
            <stop offset="1" stop-color="#a9a4c9" stop-opacity="0.5"/>
          </radialGradient>
        </defs>
        <ellipse cx="72" cy="47" rx="68" ry="40" fill="url(#violetWing)" opacity="0.8"/>
      </svg>
      <svg class="abs wash" viewBox="0 0 316 138" role="img" aria-label="Soft blue watercolour wash behind the quote">
        <defs>
          <radialGradient id="washTone" cx="0.5" cy="0.5" r="0.6">
            <stop offset="0" stop-color="#5fbde8"/>
            <stop offset="0.75" stop-color="#7ccaee"/>
            <stop offset="1" stop-color="#a9dcf3"/>
          </radialGradient>
        </defs>
        <rect x="0" y="0" width="316" height="138" rx="26" fill="url(#washTone)"/>
      </svg>
      <p class="abs quote">“Sometimes”, said Bramble<br>“The smallest thing takes up<br>the most room in your heart.”</p>
      <p class="abs body-copy treatment">Depression can be treated with counselling, “talk therapy”.<br>A check up at your doctor is advisable too.</p>
      <p class="abs lead no-discrimination">Postpartum depression doesn't discriminate. It affects women of all ages, cultural and social standing.</p>
    </section>

    <section class="panel panel--right">
      <h2 class="abs script care-title-1">Looking after</h2>
      <h2 class="abs script care-title-2">yourself...</h2>
      <div class="abs care-list body-copy">
        <div class="care-item"><span class="subhead">Rest</span>
          <p>Sleep if you can, and have a rest if you can't.<br>Nap when your baby is sleeping.</p></div>
        <div class="care-item"><span class="subhead">Diet</span>
          <p>Eat a healthy, well-balanced diet. With all the new demands on your body, good nutrition is important. Try not to skip meals.</p></div>
        <div class="care-item"><span class="subhead">Exercise</span>
          <p>Although it may be the last thing you feel like doing; some gentle exercise will help you to feel better both physically and mentally. Just going for a walk with your baby can help.</p></div>
        <div class="care-item"><span class="subhead">Meditate</span>
          <p>It may be difficult to quieten your mind;<br>a guided meditation on CD may help.</p></div>
        <div class="care-item"><span class="subhead">Stay connected</span>
          <p>Having a baby can make you feel isolated. Meet with<br>other new mothers, join a supportive mothers group.</p></div>
        <div class="care-item"><span class="subhead">Be kind to yourself</span>
          <p>You need to take care of yourself to take care of your baby. Don't load yourself up with things that really don't need to be done. Know how little can be enough.</p></div>
        <div class="care-item"><span class="subhead">Help, ask and accept</span>
          <p>Ask and accept offers of help around the home and with meals.</p>
          <p>You may not need professional help at the moment.<br>Surround yourself with people you can be honest with,<br>share how you are feeling.</p></div>
      </div>
    </section>

    <svg class="illustration" style="left:575px; top:22px;" width="185" height="130" viewBox="0 0 185 130" role="img" aria-label="Watercolour illustration of an orange and purple butterfly in flight">
      <defs>
        <linearGradient id="amberWing" x1="0" y1="1" x2="1" y2="0">
          <stop offset="0" stop-color="#7f7aa6"/>
          <stop offset="0.5" stop-color="#d47a3a"/>
          <stop offset="1" stop-color="#8d6f9a"/>
        </linearGradient>
      </defs>
      <ellipse cx="92" cy="70" rx="88" ry="45" fill="url(#amberWing)" opacity="0.75"/>
    </svg>

  </article>
</div>
</body>
</html>
```